Cleaning Company needs a new business card design

Hi, We are looking for new business card designs to update with our latest logo and company information.
We would like to see designs using the colours:
Royal Blue #4169E1 - this is our company colour so this has to be in there. Please feel free to experiment with other colours.
Must include:
Front of business card:
Logo
Back of the business card:
0800 529 6081
07438 915 702
Email: info@pkrtidyhomes.co.uk
Web: www.pkrtidyhomes.co.uk
Services:
End of Tenancy
Carpet & Upholstery
Regular & One Off
all work fully insured.
The front of the business card with the logo can be made to look raised print. The blue man to be a shiny finish.
The business card needs to be presented in a matt finish
The business must be in the following styles:
Standard Square with rounded corners.
Thank you to all that take part in this.
Target Market(s)
Men and Women of different ages in the UK.
Industry/Entity Type
House Cleaning
Contact Information for Business Card
Front of business card:
Logo
0800 529 6081
07438 915 702
Email: pkrtidy@mailbox-demo.co.uk
Services:
End of Tenancy
Carpet & Upholstery
Regular & One Off
all work fully insured.

```html
<!DOCTYPE html>
<html lang="en">
<head>
<meta charset="utf-8">
<title>PKR Tidy Homes – Business Card</title>
<link rel="stylesheet" href="https://fonts.googleapis.com/css2?family=Ubuntu:wght@300;400&display=swap">
<style>
  :root {
    --backdrop: #5c5957;
    --card-blue: #2e4898;
    --accent-blue: #29a8e0;
    --card-white: #ffffff;
    --text-grey: #5d5d63;
    --heading-blue: #2e3f9e;
  }
  * { margin: 0; padding: 0; box-sizing: border-box; }
  html, body {
    width: 1200px;
    height: 1200px;
    overflow: hidden;
    background: var(--backdrop);
    font-family: "Ubuntu", sans-serif;
  }
  .card {
    position: absolute;
    left: 262px;
    width: 676px;
    height: 406px;
    border-radius: 34px;
  }
  .card--front {
    top: 154px;
    background: var(--card-blue);
    display: flex;
    align-items: center;
    justify-content: center;
  }
  .brand {
    display: flex;
    align-items: center;
    gap: 14px;
    margin-top: -14px;
  }
  .brand__dot {
    width: 26px;
    height: 26px;
    border-radius: 50%;
    background: var(--accent-blue);
  }
  .brand__name {
    color: var(--card-white);
    font-weight: 400;
    font-size: 40px;
    letter-spacing: 0.5px;
  }
  .card--back {
    top: 640px;
    background: var(--card-white);
  }
  .services {
    position: absolute;
    left: 34px;
    top: 30px;
    font-weight: 300;
    font-size: 21px;
    line-height: 24px;
    color: var(--text-grey);
  }
  .services__title {
    color: var(--heading-blue);
    padding-left: 277px;
    margin-left: -262px;
  }
  .services__list { list-style: none; }
  .services__list li {
    position: relative;
    padding-left: 15px;
  }
  .services__list li::before {
    content: "";
    position: absolute;
    left: -2px;
    top: 8px;
    width: 10px;
    height: 10px;
    border-radius: 50%;
    background: var(--heading-blue);
  }
  .contacts {
    position: absolute;
    left: 326px;
    top: 250px;
    list-style: none;
    font-weight: 300;
    font-size: 21px;
    color: var(--text-grey);
  }
  .contacts li {
    display: flex;
    align-items: center;
    gap: 12px;
    height: 33.5px;
  }
  .contacts svg { width: 24px; height: 24px; flex: none; }
</style>
</head>
<body>
  <section class="card card--front">
    <div class="brand">
      <span class="brand__dot"></span>
      <span class="brand__name">PKR Tidy Homes Limited</span>
    </div>
  </section>

  <section class="card card--back">
    <div class="services">
      <p class="services__title" style="margin-left:0;padding-left:15px;">Services:</p>
      <ul class="services__list">
        <li>End of Tenancy</li>
        <li>Carpet &amp; Upholstery</li>
        <li>Regular &amp; One Off</li>
      </ul>
    </div>

    <ul class="contacts">
      <li>
        <svg viewBox="0 0 24 24" aria-hidden="true"><circle cx="12" cy="12" r="12" fill="#2e4898"/><path d="M8.2 6.5c.5-.4 1.2-.3 1.5.2l1.1 1.8c.3.5.2 1.1-.2 1.4l-.8.6c.5 1.4 1.6 2.6 3 3.2l.6-.8c.3-.4 1-.5 1.4-.2l1.8 1.1c.5.3.6 1 .2 1.5l-.8 1c-.6.6-1.5.8-2.3.5-3.1-1.2-5.4-3.5-6.5-6.5-.3-.8-.1-1.7.5-2.3z" fill="#fff"/></svg>
        <span>0800 529 6081</span>
      </li>
      <li>
        <svg viewBox="0 0 24 24" aria-hidden="true"><circle cx="12" cy="12" r="12" fill="#2e4898"/><rect x="8.5" y="5.5" width="7" height="13" rx="1.3" fill="#fff"/><rect x="9.7" y="7.2" width="4.6" height="8.6" fill="#2e4898"/></svg>
        <span>07438 915 702</span>
      </li>
      <li>
        <svg viewBox="0 0 24 24" aria-hidden="true"><circle cx="12" cy="12" r="12" fill="#2e4898"/><rect x="6" y="8" width="12" height="8.5" rx="1" fill="#fff"/><path d="M6.5 8.6 12 13l5.5-4.4" fill="none" stroke="#2e4898" stroke-width="1.2"/></svg>
        <span>info@pkrtidyhomes.co.uk</span>
      </li>
      <li>
        <svg viewBox="0 0 24 24" aria-hidden="true"><circle cx="12" cy="12" r="12" fill="#2e4898"/><g fill="none" stroke="#fff" stroke-width="1.1"><circle cx="12" cy="12" r="6.2"/><ellipse cx="12" cy="12" rx="2.8" ry="6.2"/><path d="M5.8 12h12.4M6.8 9h10.4M6.8 15h10.4"/></g></svg>
        <span>www.pkrtidyhomes.co.uk</span>
      </li>
    </ul>
  </section>
</body>
</html>
```